Federal Government IT Reseller - Website Overhaul

We are looking to have the website www.copperlarktech.com to have a new look and increased functionality.

Copperlark Technologies is a small US Federal Government IT hardware/software/services Value-added Reseller. Creating content is not the problem, we just need some help overhauling the site and getting some direction on what information should go where.

Short list of competitor's websites for reference:

http://www.qmtechnologies.com/
http://travelgov.com/
http://www.sandreed.com/
http://cratefinch.com/
http://www.pivot7.com/

Short list of technology partner websites for reference:

http://www.nubrix.com/
http://www.talvexa.com/
http://www.morlun.com/

Target Market(s)

US Federal Government - Bureau of Coastal Works and Civilian Agencies.

Large Prime Contractors - Harwell Dunmore, Castleby Renfrew, Tavlor

IT End Users and Purchasing Departments

Industry/Entity Type

Government

Requirements
Must have
• Social media buttons on homepage and contact us page: WorkLoop, Kinpage, Chirpline.
• News page for blog posts/Press releases/etc (comments turned off).
• Copperlark Logo, Green/Plum color scheme, please see attached files for reference.
• A more functional Solutions page that is easier to digest and look at. We have many more solutions that we'd like to display but this was the best we could do for a one page mock up. Some expansion buttons for each header would be excellent.
Nice to have
• A more functional contact us page. We have more content (2nd office location, additional e-mail addresses, etc) - but we know how to use Wordpress, just looking for something new to work off of.
• A functional support page, we plan on using a HelpMoor form on the support page.
• A more functional Clients page that can appropriately incorporate references and highlight large contracts/contract vehicles that Copperlark Technologies has been awarded.

```html
<!DOCTYPE html>
<html lang="en">
<head>
<meta charset="utf-8">
<title>Copperlark Technologies</title>
<link rel="stylesheet" href="https://fonts.googleapis.com/css2?family=Exo+2:wght@300;400;600;700&family=Open+Sans:wght@400;600;700&family=Cousine:ital@1&display=swap">
<style>
:root{
  --green:#8fbf1f;
  --green-dark:#6f9a10;
  --green-text:#6aa319;
  --ink:#222;
  --body:#333;
  --panel:#fff;
  --page:#fff;
  --dark:#262626;
  --darker:#161616;
  --band:#2b2b2b;
  --muted:#8a8a8a;
  --quote-bg:#e6e6e6;
}
*{margin:0;padding:0;box-sizing:border-box}
html,body{width:941px;height:1200px;overflow:hidden;background:var(--page)}
body{position:relative;font-family:Arial,Helvetica,sans-serif;color:var(--body)}
.abs{position:absolute}

/* header */
.header{left:0;top:0;width:941px;height:125px;background:linear-gradient(#fff,#f3f3f3)}
.brand{left:82px;top:24px;display:flex;align-items:center;gap:8px}
.brand-dot{width:22px;height:22px;border-radius:50%;background:var(--green)}
.brand-name{font-family:'Open Sans',sans-serif;font-weight:700;font-size:24px;color:#2a2a2a;letter-spacing:-.5px}
.tagline{left:254px;top:16px;font-family:'Cousine',monospace;font-style:italic;font-size:9.5px;line-height:15px;letter-spacing:1.6px;color:#8a8a8a;text-transform:uppercase}
.search{left:685px;top:35px;width:174px;height:29px;border-radius:15px;border:1px solid #d6d6d6;background:linear-gradient(#e9e9e9,#f8f8f8);box-shadow:inset 0 1px 2px rgba(0,0,0,.12)}
.search svg{position:absolute;left:9px;top:7px}

/* nav */
.nav{left:80px;top:101px;width:781px;height:31px;background:linear-gradient(#a3cf2e,var(--green));border-bottom:2px solid var(--green-dark);display:flex;align-items:center;z-index:2}
.nav a{color:#fff;font-size:10px;font-weight:700;text-decoration:none;padding:0 23px;height:17px;line-height:17px;border-right:1px solid rgba(255,255,255,.45)}
.nav a:first-child{padding-left:21px}
.nav a:last-child{border-right:none}

/* hero */
.hero{left:0;top:125px;width:941px;height:323px;background:linear-gradient(100deg,#231d17 0%,#3a2f24 35%,#5a4a38 60%,#4a3d30 80%,#2a231c 100%)}
.hero-title{left:92px;top:192px;font-family:'Exo 2',sans-serif;color:#fff;font-size:21px;line-height:30px;font-weight:300;letter-spacing:.6px}
.hero-title b{font-weight:700;font-size:24px}
.hero-copy{left:92px;top:260px;width:320px;color:#fff;font-size:10.5px;line-height:17px}
.hero-btn{left:95px;top:344px;width:194px;height:47px;border-radius:24px;background:linear-gradient(#b6e03c,#7fb01a);border:2px solid #c7e86a;box-shadow:0 2px 4px rgba(0,0,0,.5);font-family:'Exo 2',sans-serif;font-weight:600;font-size:22px;color:#fff;padding-left:12px;line-height:43px;letter-spacing:.5px}
.hero-btn .arrow{position:absolute;right:12px;top:9px;width:25px;height:25px;border-radius:50%;background:#fff}

/* tabs panel */
.panel{left:90px;top:464px;width:758px;height:269px;background:var(--panel);border:1px solid #e2e2e2;box-shadow:0 0 6px rgba(0,0,0,.06)}
.tabs{left:0;top:0;width:756px;height:40px;background:linear-gradient(#ececec,#dedede);display:flex}
.tab{height:40px;line-height:42px;font-size:10.5px;font-weight:700;letter-spacing:.7px;color:#333;padding:0 16px;border-right:1px solid #cfcfcf}
.tab.active{background:#fff;width:164px;padding-left:28px}
.tab:nth-child(2){width:125px;padding-left:13px}
.tab:nth-child(3){width:193px;padding-left:13px}
.panel h2{left:18px;top:60px;font-family:'Open Sans',sans-serif;font-weight:600;font-size:20px;color:#333;white-space:nowrap}
.panel h2 span{color:var(--green-text)}
.panel .copy{left:22px;top:99px;width:470px;font-size:11px;line-height:17px;color:#333}
.panel .copy p+p{margin-top:17px}
.video{left:499px;top:67px;width:243px;height:162px}
.video .frame{width:243px;height:145px;background:linear-gradient(120deg,#d9d2c6,#b8aea0 50%,#8e7f70)}
.video .controls{width:243px;height:17px;background:linear-gradient(#3a3a3a,#111);display:flex;align-items:center;padding:0 4px;gap:6px}

/* features band */
.features{left:90px;top:733px;width:758px;height:68px;background:linear-gradient(#333,#1e1e1e);display:flex}
.feat-col{flex:none;height:68px;padding-top:14px;border-right:1px solid #444;font-family:'Open Sans',sans-serif;font-weight:700;font-size:13px;color:#fff}
.feat-col:last-child{border-right:none}
.feat-col li{list-style:none;display:flex;align-items:center;gap:10px;height:23px}

/* testimonial */
.quote{left:90px;top:832px;width:758px;height:131px;background:var(--quote-bg);border:1px solid #d4d4d4}
.quote p{position:absolute;left:20px;top:34px;width:716px;text-align:center;font-family:'Open Sans',sans-serif;font-size:16.5px;line-height:22px;color:#222}
.qmark{width:54px;height:54px;border-radius:50%;background:#fff;font-family:'Open Sans',sans-serif;font-weight:700;font-size:40px;color:#555;text-align:center;line-height:66px}
.qmark.open{left:19px;top:-27px}
.qmark.close{left:680px;top:103px}
.author{left:0;top:978px;width:941px;text-align:center;font-family:'Open Sans',sans-serif;font-size:15px;color:#222}
.author b{font-weight:700}

/* footer */
.footer{left:2px;top:1024px;width:939px;height:149px;background:var(--dark);border-top:2px solid #111}
.fcol{top:0;height:149px}
.fcol + .fcol{border-left:1px solid #3a3a3a}
.footer h3{font-family:'Open Sans',sans-serif;font-weight:400;color:#fff}
.footer small,.footer li{font-family:'Open Sans',sans-serif;font-size:9.5px;line-height:12px;color:#7d7d7d}
.footer ul{list-style:none}
.footer li::before{content:"•";margin-right:6px;color:#666}
.learn{color:var(--green);font-size:9.5px;font-family:'Open Sans',sans-serif}
.phone{font-family:'Open Sans',sans-serif;font-size:19px;color:#fff}
.social span{display:inline-block;width:12px;height:12px;margin-left:3px;vertical-align:middle}
.bottom{left:2px;top:1173px;width:939px;height:27px;background:var(--darker);text-align:center;font-size:9.5px;line-height:27px;color:#888}
</style>
</head>
<body>

<header class="abs header">
  <div class="abs brand"><span class="brand-dot"></span><span class="brand-name">Copperlark</span></div>
  <div class="abs tagline">An IT value-added<br>reseller to the<br>U.S. government<br>and its integrators</div>
  <div class="abs search">
    <svg width="15" height="15" viewBox="0 0 15 15"><circle cx="6" cy="6" r="4.5" fill="none" stroke="#333" stroke-width="1.6"/><line x1="9.3" y1="9.3" x2="14" y2="14" stroke="#333" stroke-width="2.2" stroke-linecap="round"/></svg>
  </div>
</header>

<nav class="abs nav">
  <a>HOME</a><a>SOLUTIONS</a><a>CLIENTS</a><a>COMPANY</a><a>EVENTS</a><a>CONTACT US</a>
</nav>

<section class="abs hero" role="img" aria-label="Photo of a man working at a desktop computer in a wooden workshop"></section>
<h1 class="abs hero-title"><b>Top 10 Free</b> Must-have Web<br>Apps for Entrepreneurs</h1>
<p class="abs hero-copy">A cost-effective, easy-to-use solution that makes backup and disaster recover a reality even for small business. Choose the edition that's right for your platform</p>
<div class="abs hero-btn">Information
  <span class="arrow"><svg width="25" height="25" viewBox="0 0 25 25"><path d="M10 7l6 5.5-6 5.5" fill="none" stroke="#8fbf1f" stroke-width="3"/></svg></span>
</div>

<section class="abs panel">
  <div class="abs tabs">
    <div class="tab active">COMPANY VISION</div>
    <div class="tab">NETWORKING</div>
    <div class="tab">MANAGEMENT EXPERIENCE</div>
  </div>
  <h2 class="abs"><span>Our best car rental</span> rates, guaranteed</h2>
  <div class="abs copy">
    <p>Lorem Ipsum is simply dummy text of the printing and typesetting industry. Lorem Ipsum has been the industry's standard dummy text ever since the 1500s, when an unknown printer took a galley of type and scrambled it to make a type specimen book.</p>
    <p>It has survived not only five centuries, but also the leap into electronic typesetting, remaining essentially unchanged. It was popularised in the 1960s with the release of Dryset sheets containing Lorem Ipsum passages.</p>
  </div>
  <div class="abs video">
    <div class="frame" role="img" aria-label="Video still of three colleagues discussing work at a table" style="position:relative">
      <svg style="position:absolute;left:85px;top:41px" width="60" height="60" viewBox="0 0 60 60"><circle cx="30" cy="30" r="29" fill="#1a1a1a" opacity=".9"/><path d="M23 17l20 13-20 13z" fill="#fff"/></svg>
    </div>
    <div class="controls">
      <svg width="13" height="13" viewBox="0 0 13 13"><circle cx="6.5" cy="6.5" r="6" fill="#555"/><path d="M5 4l4 2.5-4 2.5z" fill="#fff"/></svg>
      <svg width="90" height="6"><rect width="90" height="3" y="1.5" fill="#555"/><circle cx="3" cy="3" r="3" fill="#f60"/></svg>
      <span style="font-size:6px;color:#aaa">-0:00</span>
      <span style="font-size:8px;color:#ccc;font-style:italic">i</span>
      <svg width="10" height="7"><rect width="10" height="7" fill="#ccc"/></svg>
      <svg width="34" height="8"><path d="M0 2h3l3-2v8l-3-2H0z" fill="#ccc"/><g fill="#f60"><rect x="10" y="1" width="2" height="6"/><rect x="14" y="1" width="2" height="6"/><rect x="18" y="1" width="2" height="6"/><rect x="22" y="1" width="2" height="6"/><rect x="26" y="1" width="2" height="6"/></g></svg>
      <svg width="10" height="8"><rect x=".5" y=".5" width="9" height="7" fill="none" stroke="#ccc"/></svg>
    </div>
  </div>
</section>

<section class="abs features">
  <ul class="feat-col" style="width:237px;padding-left:24px">
    <li><svg width="14" height="11"><path d="M1 6l4 4 8-9" fill="none" stroke="#8fbf1f" stroke-width="2.4"/></svg>100% Network Uptime SLA</li>
    <li><svg width="14" height="11"><path d="M1 6l4 4 8-9" fill="none" stroke="#8fbf1f" stroke-width="2.4"/></svg>ISO 9001:2008 Certified</li>
  </ul>
  <ul class="feat-col" style="width:278px;padding-left:25px">
    <li><svg width="14" height="11"><path d="M1 6l4 4 8-9" fill="none" stroke="#8fbf1f" stroke-width="2.4"/></svg>24/7 ITIL Technical Support</li>
    <li><svg width="14" height="11"><path d="M1 6l4 4 8-9" fill="none" stroke="#8fbf1f" stroke-width="2.4"/></svg>3 SSAE-16 Certified Data Centers</li>
  </ul>
  <ul class="feat-col" style="width:243px;padding-left:24px">
    <li><svg width="14" height="11"><path d="M1 6l4 4 8-9" fill="none" stroke="#8fbf1f" stroke-width="2.4"/></svg>Coast-to-coast IP Backbone</li>
    <li><svg width="14" height="11"><path d="M1 6l4 4 8-9" fill="none" stroke="#8fbf1f" stroke-width="2.4"/></svg>Award Winning Since 1996</li>
  </ul>
</section>

<section class="abs quote">
  <div class="abs qmark open">“</div>
  <p>We had been badly let down by several companies over the last few years, but last year I found Tollvane Servers on Searchly &amp; within 15 minutes I had recieved a response back from Marcus with full pricing &amp; my server is still running perfectly, with no downtime...</p>
  <div class="abs qmark close" style="clip-path:inset(0 0 27px 0)">”</div>
  <svg class="abs" style="left:252px;top:129px" width="40" height="20" viewBox="0 0 40 20"><path d="M0 0L28 19 24 0z" fill="#e6e6e6" stroke="#d4d4d4"/><rect x="1" y="-1" width="22" height="2" fill="#e6e6e6"/></svg>
</section>
<div class="abs author"><b>Alan Brook</b> brookpoint.com</div>

<footer class="abs footer">
  <div class="abs fcol" style="left:0;width:333px;padding:20px 0 0 95px">
    <h3 style="font-size:19px">Keep it Simple!</h3>
    <small style="display:block;margin-top:12px;width:230px">The web changes people and the things they do. This is why we develop increasingly reliable, easy-to-use and intuitive services.</small>
    <div class="learn" style="margin-top:12px">› &nbsp;Learn more</div>
  </div>
  <div class="abs fcol" style="left:333px;width:296px;padding:25px 0 0 27px">
    <h3 style="font-size:12px">About Tollvane Servers</h3>
    <div style="display:flex;gap:14px;margin-top:8px">
      <ul style="width:104px"><li>About Us</li><li>Contact Us</li><li>Terms &amp; Conditions</li></ul>
      <ul><li>Support</li><li>Why choose us</li><li>Service level agreement</li></ul>
    </div>
    <div class="social" style="margin-top:12px"><small>© 2012 Tollvane Servers. &nbsp;All Rights Reserved.</small>
      <span style="background:#3b5a9a;margin-left:8px"></span><span style="background:#3fa9dd"></span><span style="background:#e8761c"></span></div>
  </div>
  <div class="abs fcol" style="left:629px;width:310px;padding:25px 0 0 27px">
    <h3 style="font-size:12px">Information</h3>
    <small style="display:block;margin-top:10px;width:200px">Contact Us via our Support Ticket System in your <span style="color:#ddd">Online Control Panel</span> or alternatively call us on the number below:</small>
    <div class="phone" style="margin-top:12px">+44 (0)1632 960 418</div>
  </div>
</footer>
<div class="abs bottom">Copyright© 2005, 2010, Copperlark and/or its affiliates. All rights reserved.</div>

</body>
</html>
```